Stationary For Harbor Allies
Harbor Allies
Project: Stationary For Harbor Allies
Stationary For Harbor Allies - Consulting
Creative Brief
Professional
Lou Brannick
President
547 Marlow Ln Spring Branch, TX 78070
lbrannick@harborallies4.com
www.harborallies4.com
I will need letterhead and envelopes as well as business cards. Feel free to try different fonts.
quelnor42 quelnor42
Designers, Please focus more on the letterhead and envelopes than the business cards. Thanks!

```html
<!DOCTYPE html>
<html lang="en">
<head>
<meta charset="utf-8">
<title>Harbor Allies — Business Card</title>
<link rel="stylesheet" href="https://fonts.googleapis.com/css2?family=Poppins:wght@400;500;600&display=swap">
<style>
  :root {
    --page-bg: #e9e7e3;
    --card-white: #ffffff;
    --brand-blue: #2f5a8e;
    --band-grey: #9ea3a8;
    --light-grey: #d5d8db;
    --text-grey: #6d7278;
    --on-blue: #ffffff;
  }
  * { box-sizing: border-box; margin: 0; padding: 0; }
  html, body {
    width: 1200px; height: 901px; overflow: hidden;
    background: var(--page-bg);
    font-family: "Poppins", sans-serif;
  }
  .business-card {
    position: absolute; left: 150px; top: 193px;
    width: 900px; height: 514px;
    background: var(--card-white);
    border-radius: 34px; overflow: hidden;
    box-shadow: 0 8px 26px rgba(0,0,0,0.14);
  }
  .card-shapes { position: absolute; inset: 0; }
  .brand {
    position: absolute; left: 70px; top: 178px;
    display: flex; align-items: center; gap: 18px;
  }
  .brand-dot {
    width: 64px; height: 64px; border-radius: 50%;
    background: var(--brand-blue);
  }
  .brand-name {
    font-size: 40px; font-weight: 500; color: var(--brand-blue);
    letter-spacing: 0.5px;
  }
  .person { position: absolute; left: 70px; top: 338px; }
  .person-name {
    font-size: 27px; font-weight: 600; color: var(--brand-blue);
    letter-spacing: 1.5px; text-transform: uppercase;
  }
  .person-title { font-size: 19px; color: var(--text-grey); margin-top: 2px; }
  .contact {
    position: absolute; right: 48px; top: 68px;
    color: var(--on-blue); text-align: right; font-size: 16px; line-height: 1.35;
  }
  .contact-address { margin-bottom: 40px; font-size: 17px; }
  .contact-list { list-style: none; }
  .contact-list li {
    display: flex; justify-content: flex-end; align-items: center;
    gap: 12px; height: 34px; white-space: nowrap;
  }
  .contact-list svg { width: 18px; height: 18px; flex: none; }
</style>
</head>
<body>
  <div class="business-card">
    <svg class="card-shapes" viewBox="0 0 900 514" aria-hidden="true">
      <path d="M600,0 C570,140 500,330 320,514 L360,514 C540,330 610,140 640,0 Z" fill="var(--light-grey)"/>
      <path d="M636,0 C606,140 536,330 356,514 L412,514 C590,330 650,140 672,0 Z" fill="var(--band-grey)"/>
      <path d="M668,0 C640,140 580,330 404,514 L900,514 L900,0 Z" fill="var(--brand-blue)"/>
    </svg>

    <div class="brand">
      <div class="brand-dot"></div>
      <div class="brand-name">Harbor Allies</div>
    </div>

    <div class="person">
      <div class="person-name">Lou Brannick</div>
      <div class="person-title">President</div>
    </div>

    <div class="contact">
      <div class="contact-address">547 Marlow Ln<br>Spring Branch, TX 78070</div>
      <ul class="contact-list">
        <li>210 555 0147
          <svg viewBox="0 0 24 24"><path d="M6 3l4 4-2 3c1 2 4 5 6 6l3-2 4 4-3 3C10 21 3 14 3 6z" fill="none" stroke="currentColor" stroke-width="2"/></svg>
        </li>
        <li>210 555 0147
          <svg viewBox="0 0 24 24"><rect x="7" y="2" width="10" height="20" rx="2" fill="none" stroke="currentColor" stroke-width="2"/><circle cx="12" cy="18" r="1.2" fill="currentColor"/></svg>
        </li>
        <li>210 555 0147
          <svg viewBox="0 0 24 24"><rect x="3" y="8" width="18" height="11" rx="1" fill="none" stroke="currentColor" stroke-width="2"/><rect x="7" y="3" width="10" height="5" fill="none" stroke="currentColor" stroke-width="2"/></svg>
        </li>
        <li>lbrannick@harborallies4.com
          <svg viewBox="0 0 24 24"><rect x="3" y="5" width="18" height="14" rx="1" fill="none" stroke="currentColor" stroke-width="2"/><path d="M3 6l9 7 9-7" fill="none" stroke="currentColor" stroke-width="2"/></svg>
        </li>
        <li>www.harborallies4.com
          <svg viewBox="0 0 24 24"><circle cx="12" cy="12" r="9" fill="none" stroke="currentColor" stroke-width="2"/><path d="M3 12h18M12 3c3 3 3 15 0 18M12 3c-3 3-3 15 0 18" fill="none" stroke="currentColor" stroke-width="1.5"/></svg>
        </li>
      </ul>
    </div>
  </div>
</body>
</html>
```